Billboard design for a new container self storage

I’m after a sign designing for a new container storage opening. located in the heart of Scunthorpe. Open 24/7. Brand new containers. On site security. Best prices guaranteed

Open 24/7
Safe secure self storage
Best prices Guaranteed
Site address
Tarbury Row
Scunthorpe
ZX48 2QT
Also include next left and an arrow
Dark green/ grey and fluorescent lime green

Contact - info@marshvaleunits.co.uk
07946201583

Website colours attached

Requirements
Must have
• Instagram logo @Marshvaleselfstorage

```html
<!DOCTYPE html>
<html lang="en">
<head>
<meta charset="utf-8">
<title>Marshvale Self Storage Billboard</title>
<link rel="stylesheet" href="https://fonts.googleapis.com/css2?family=Montserrat:wght@500;700;800&family=Roboto+Condensed:wght@700&display=swap">
<style>
  :root {
    --lime: #d8f75a;
    --lime-bright: #d4f53c;
    --forest: #1f2e0f;
    --ink: #2a2a2a;
    --white: #ffffff;
    --backdrop: #e9ecef;
  }
  * { margin: 0; padding: 0; box-sizing: border-box; }
  html, body { width: 1200px; height: 900px; overflow: hidden; }
  body { background: var(--backdrop); position: relative; }

  .billboard {
    position: absolute; left: 0; top: 154px;
    width: 1200px; height: 592px;
    background: var(--white);
    box-shadow: 0 6px 24px rgba(0,0,0,0.18);
    overflow: hidden;
  }
  .billboard-art { position: absolute; inset: 0; width: 100%; height: 100%; }

  .brand-name {
    position: absolute; left: 0; width: 475px; top: 44px;
    text-align: center;
    font-family: "Montserrat", sans-serif; font-weight: 700;
    font-size: 36px; letter-spacing: 1px; color: var(--forest);
  }
  .social-handle {
    position: absolute; left: 0; width: 475px; top: 96px;
    display: flex; justify-content: center; align-items: center; gap: 7px;
    font-family: "Montserrat", sans-serif; font-weight: 700;
    font-size: 16px; color: var(--forest);
  }
  .social-mark {
    width: 14px; height: 14px; border-radius: 50%;
    background: var(--forest); flex: none;
  }

  .feature-list {
    position: absolute; left: 70px; top: 146px; list-style: none;
    font-family: "Roboto Condensed", sans-serif; font-weight: 700;
    font-size: 21px; color: var(--forest);
  }
  .feature-list li {
    display: flex; align-items: center; height: 35.5px; gap: 6px;
  }
  .tick { width: 22px; height: 22px; flex: none; }
  .direction-arrow { width: 46px; height: 22px; margin-left: 6px; flex: none; }

  .contact-label {
    position: absolute; left: 74px; top: 441px;
    font-family: "Montserrat", sans-serif; font-weight: 800;
    font-size: 27px; color: var(--white);
  }
  .phone {
    position: absolute; left: 44px; top: 484px;
    display: flex; align-items: center; gap: 8px;
    font-family: "Montserrat", sans-serif; font-weight: 700;
    font-size: 42px; color: var(--ink); letter-spacing: 0.5px;
  }
  .phone-icon { width: 42px; height: 42px; }
  .email {
    position: absolute; left: 50px; top: 543px;
    font-family: "Montserrat", sans-serif; font-weight: 500;
    font-size: 21px; color: var(--forest);
  }
</style>
</head>
<body>
  <section class="billboard">
    <svg class="billboard-art" viewBox="0 0 1280 632" preserveAspectRatio="none">
      <defs>
        <linearGradient id="panel-fill" x1="0" y1="0" x2="1" y2="1">
          <stop offset="0" stop-color="#e2fa7a"/>
          <stop offset="1" stop-color="#cdee4e"/>
        </linearGradient>
        <linearGradient id="yard-fill" x1="0" y1="0" x2="0" y2="1">
          <stop offset="0" stop-color="#d9d9d9"/>
          <stop offset="0.45" stop-color="#8a8a8a"/>
          <stop offset="1" stop-color="#4a4a4a"/>
        </linearGradient>
        <linearGradient id="port-fill" x1="0" y1="0" x2="0" y2="1">
          <stop offset="0" stop-color="#5b7890"/>
          <stop offset="0.55" stop-color="#9a6a4a"/>
          <stop offset="1" stop-color="#3d3f44"/>
        </linearGradient>
        <linearGradient id="stack-fill" x1="0" y1="0" x2="0" y2="1">
          <stop offset="0" stop-color="#c9785a"/>
          <stop offset="0.45" stop-color="#3f6fb5"/>
          <stop offset="1" stop-color="#3a4150"/>
        </linearGradient>
      </defs>

      <polygon points="0,143 430,143 690,315 600,487 0,487" fill="url(#panel-fill)"/>

      <polygon points="45,468 318,468 300,507 35,507 48,487" fill="var(--forest)"/>
      <polygon points="0,572 512,572 490,610 0,610" fill="var(--lime)"/>

      <polygon points="575,0 985,0 1215,310 1000,632 590,632 775,310"
               fill="url(#yard-fill)" role="img"
               aria-label="Black and white photo of stacked shipping containers with a container handler"/>

      <polyline points="505,0 722,306 505,632" fill="none" stroke="var(--lime-bright)" stroke-width="12"/>
      <polyline points="538,0 752,308 545,632" fill="none" stroke="var(--forest)" stroke-width="20"/>

      <polyline points="1000,0 1228,310 1015,632" fill="none" stroke="var(--forest)" stroke-width="14"/>
      <polyline points="1022,0 1250,310 1037,632" fill="none" stroke="var(--lime-bright)" stroke-width="10"/>

      <polygon points="410,215 487.5,80 642.5,80 720,215 642.5,350 487.5,350" fill="var(--white)"/>
      <polygon points="425,215 495,90 635,90 705,215 635,340 495,340" fill="var(--forest)"/>
      <polygon points="437,215 501,101 629,101 693,215 629,329 501,329" fill="var(--lime-bright)"/>
      <polygon points="447,215 506,110 624,110 683,215 624,320 506,320" fill="url(#port-fill)"
               role="img" aria-label="Photo of a port crane above rows of coloured containers at dusk"/>

      <polygon points="975,460 1045,335 1185,335 1255,460 1185,585 1045,585" fill="var(--white)"/>
      <polygon points="989,460 1052,348 1178,348 1241,460 1178,572 1052,572" fill="var(--forest)"/>
      <polygon points="1000,460 1057.5,358 1172.5,358 1230,460 1172.5,562 1057.5,562" fill="var(--lime-bright)"/>
      <polygon points="1009,460 1062,366 1168,366 1221,460 1168,554 1062,554" fill="url(#stack-fill)"
               role="img" aria-label="Photo of blue container stacks under a sunset sky"/>
    </svg>

    <div class="brand-name">MARSHVALE</div>
    <div class="social-handle"><span class="social-mark"></span>@Marshvaleselfstorage</div>

    <ul class="feature-list">
      <li><svg class="tick" viewBox="0 0 22 22"><rect x="2" y="5" width="15" height="15" fill="none" stroke="var(--forest)" stroke-width="2"/><path d="M5 11 L10 17 L20 2" fill="none" stroke="var(--forest)" stroke-width="3"/></svg>OPEN 24/7</li>
      <li><svg class="tick" viewBox="0 0 22 22"><rect x="2" y="5" width="15" height="15" fill="none" stroke="var(--forest)" stroke-width="2"/><path d="M5 11 L10 17 L20 2" fill="none" stroke="var(--forest)" stroke-width="3"/></svg>SAFE SECURE SELF STORAGE</li>
      <li><svg class="tick" viewBox="0 0 22 22"><rect x="2" y="5" width="15" height="15" fill="none" stroke="var(--forest)" stroke-width="2"/><path d="M5 11 L10 17 L20 2" fill="none" stroke="var(--forest)" stroke-width="3"/></svg>BEST PRICES GUARANTEED</li>
      <li><svg class="tick" viewBox="0 0 22 22"><rect x="2" y="5" width="15" height="15" fill="none" stroke="var(--forest)" stroke-width="2"/><path d="M5 11 L10 17 L20 2" fill="none" stroke="var(--forest)" stroke-width="3"/></svg>SITE ADDRESS</li>
      <li><svg class="tick" viewBox="0 0 22 22"><rect x="2" y="5" width="15" height="15" fill="none" stroke="var(--forest)" stroke-width="2"/><path d="M5 11 L10 17 L20 2" fill="none" stroke="var(--forest)" stroke-width="3"/></svg>TARBURY ROW</li>
      <li><svg class="tick" viewBox="0 0 22 22"><rect x="2" y="5" width="15" height="15" fill="none" stroke="var(--forest)" stroke-width="2"/><path d="M5 11 L10 17 L20 2" fill="none" stroke="var(--forest)" stroke-width="3"/></svg>SCUNTHORPE</li>
      <li><svg class="tick" viewBox="0 0 22 22"><rect x="2" y="5" width="15" height="15" fill="none" stroke="var(--forest)" stroke-width="2"/><path d="M5 11 L10 17 L20 2" fill="none" stroke="var(--forest)" stroke-width="3"/></svg>ZX48 2QT</li>
      <li><svg class="tick" viewBox="0 0 22 22"><rect x="2" y="5" width="15" height="15" fill="none" stroke="var(--forest)" stroke-width="2"/><path d="M5 11 L10 17 L20 2" fill="none" stroke="var(--forest)" stroke-width="3"/></svg>NEXT LEFT
        <svg class="direction-arrow" viewBox="0 0 46 22" role="img" aria-label="Arrow pointing left"><polygon points="0,11 14,0 14,7 46,7 46,15 14,15 14,22" fill="var(--forest)"/></svg>
      </li>
    </ul>

    <div class="contact-label">Contact Us :</div>

    <div class="phone">
      <svg class="phone-icon" viewBox="0 0 42 42">
        <path d="M9 4 L15 4 L18 13 L13 16 Q17 25 26 29 L29 24 L38 27 L38 33 Q37 38 31 38 Q8 35 4 11 Q4 5 9 4 Z" fill="var(--forest)"/>
        <path d="M24 8 Q33 9 34 18" fill="none" stroke="var(--forest)" stroke-width="3"/>
        <path d="M24 2 Q39 3 40 18" fill="none" stroke="var(--forest)" stroke-width="3"/>
      </svg>
      <span>07946201583</span>
    </div>

    <div class="email">info@marshvaleunits.co.uk</div>
  </section>
</body>
</html>
```